Business Card Design Project

Hi!
Looking for a business card design for my acupuncture/remedial massage business using a logo I've just had designed through this site!
I'd like the following details included:
Logo (obviously)
My name - Miranda Pellowtane
Clinic details -Complementary and Traditional Chinese Medicine Haven
42 Brindlewood Road
Ashcombe Vale 3162
03 9471 6820
Website - www.pellowtanewell.com.au
I have the logo design in two different colour combinations, one predominantly green, and the other in reverse colours. I was thinking that the green logo would take up one whole side of the business card, then we could include the reverse logo on the more detailed side. I'd like to see how that looks.
I also had the idea that the heart in the logo could be printed in metallic red (depending on cost). Not sure if that comes into play now or at the printers.
Thanks!

```html
<!DOCTYPE html>
<html lang="en">
<head>
<meta charset="utf-8">
<title>Pellowtane Well – Business Card</title>
<link href="https://fonts.googleapis.com/css2?family=Lato:wght@400&display=swap" rel="stylesheet">
<style>
  :root {
    --brand-green: #2bb68a;
    --paper: #ffffff;
    --card-edge: #e2e2e2;
    --canvas: #ffffff;
    --ink-light: #ffffff;
    --label-tint: rgba(255,255,255,0.35);
  }
  * { margin: 0; padding: 0; box-sizing: border-box; }
  html, body {
    width: 984px; height: 1200px; overflow: hidden;
    background: var(--canvas);
    font-family: "Lato", "Gill Sans", sans-serif;
  }
  .canvas { position: relative; width: 984px; height: 1200px; }

  .card { position: absolute; left: 25px; width: 934px; height: 567px; }
  .card--front { top: 1px; background: var(--paper); border: 2px solid var(--card-edge); }
  .card--back { top: 604px; background: var(--brand-green); }

  .brand-name {
    position: absolute; left: 0; right: 0; text-align: center;
    font-weight: 400; letter-spacing: 1px; line-height: 1;
  }
  .card--front .brand-name { top: 256px; font-size: 56px; color: var(--brand-green); }
  .card--back .brand-name { top: 110px; font-size: 38px; color: var(--ink-light); }

  .card__divider {
    position: absolute; left: 0; right: 0; top: 230px;
    height: 2px; background: var(--ink-light);
  }

  .contact-list { position: absolute; left: 0; top: 293px; list-style: none; color: var(--ink-light); }
  .contact-item { position: relative; padding-left: 101px; font-size: 21px; line-height: 37px; }
  .contact-item + .contact-item { margin-top: 10px; }
  .contact-icon { position: absolute; left: 30px; width: 44px; height: 34px; }
  .contact-item--address .contact-icon { top: 18px; }
  .contact-item--phone .contact-icon { top: 2px; }
  .contact-item--web .contact-icon { top: 2px; }

  .person { position: absolute; right: 64px; top: 400px; text-align: right; color: var(--ink-light); }
  .person__title-art {
    display: block; margin-left: auto; margin-bottom: 8px;
    width: 120px; height: 20px; background: var(--label-tint); border-radius: 10px;
  }
  .person__name { font-size: 21px; }
</style>
</head>
<body>
<main class="canvas">

  <section class="card card--front" aria-label="Business card front">
    <div class="brand-name">Pellowtane Well</div>
  </section>

  <section class="card card--back" aria-label="Business card back">
    <div class="brand-name">Pellowtane Well</div>
    <div class="card__divider"></div>

    <ul class="contact-list">
      <li class="contact-item contact-item--address">
        <svg class="contact-icon" viewBox="0 0 44 34" aria-hidden="true">
          <rect x="4" y="5" width="30" height="22" fill="#f4f4f4" stroke="#c9c9c9"/>
          <polyline points="4,5 19,18 34,5" fill="none" stroke="#a9a9a9" stroke-width="1.5"/>
          <path d="M34 22h8M38 18v8" stroke="#1e8a62" stroke-width="3"/>
        </svg>
        Complementary and Traditional Chinese Medicine Haven<br>
        42 Brindlewood Road, Ashcombe Vale 3162
      </li>
      <li class="contact-item contact-item--phone">
        <svg class="contact-icon" viewBox="0 0 44 34" aria-hidden="true">
          <rect x="10" y="10" width="30" height="18" rx="3" fill="#f4f4f4" stroke="#9a9a9a"/>
          <rect x="16" y="14" width="18" height="6" fill="#ccc"/>
          <path d="M4 4c0 0 2-2 5 0v22c-3 2-5 0-5 0z" fill="#e9e9e9" stroke="#9a9a9a"/>
        </svg>
        03 9471 6820
      </li>
      <li class="contact-item contact-item--web">
        <svg class="contact-icon" viewBox="0 0 44 34" aria-hidden="true">
          <path d="M6 26h30l4 5H2z" fill="#e0e0e0" stroke="#999"/>
          <rect x="9" y="8" width="24" height="18" fill="#dcdcdc" stroke="#999"/>
          <circle cx="21" cy="13" r="9" fill="#2f6fb8" stroke="#1c4a80"/>
          <path d="M15 10c3 1 5-1 7 1s-1 4 2 5" fill="none" stroke="#4fae4f" stroke-width="2"/>
        </svg>
        www.pellowtanewell.com.au
      </li>
    </ul>

    <div class="person">
      <span class="person__title-art" role="img" aria-label="Handwritten job title: manager"></span>
      <div class="person__name">Miranda Pellowtane</div>
    </div>
  </section>

</main>
</body>
</html>
```